Family owned plumbing contractor needs eye catching business card design

Business cards that are unique, eye catching, and provide customers with general company information, such as name, address, phone number, website, employee name/title, cell phone #, & email address. We are transitioning to a new logo that utilizes a more retro feel, so we are interested in seeing some cool old school designs in the mix. We are liking the dark background on some of the samples on this website. If that is workable with our artwork, we would like to see that incorporated into the design.
Contact Information for Business Card
Copperline Pipeworks, Inc.
www.copperlinepipeworks.example
(555) 630-2918 phone
Nevada License #64205
California License #5870413
Glen Harwick, President
(555) 418-9063 cell
glen@copperlinepipeworks.example
Residential * Commercial * Service
Requirements
Must have
- The business card details listed above & logo provided.
Nice to have
- I made some notes about color options in the description.

```html
<!DOCTYPE html>
<html lang="en">
<head>
<meta charset="utf-8">
<title>Copperline Pipeworks business cards</title>
<link rel="stylesheet" href="https://fonts.googleapis.com/css2?family=Lato:wght@400;700&display=swap">
<style>
  :root {
    --bg: #8a898e;
    --teal: #7fc8bb;
    --teal-dark: #5fb8a8;
    --slate: #4f6f8c;
    --paper: #ffffff;
    --ink: #6b6b6b;
    --shadow: rgba(0, 0, 0, 0.28);
  }
  * { margin: 0; padding: 0; box-sizing: border-box; }
  html, body {
    width: 1200px; height: 895px; overflow: hidden;
    background: var(--bg);
    font-family: "Lato", sans-serif;
  }
  .stage {
    width: 1200px; height: 895px;
    display: flex; align-items: center; justify-content: center; gap: 50px;
  }
  .card {
    width: 525px; height: 300px;
    position: relative;
    box-shadow: 0 10px 24px var(--shadow);
    overflow: hidden;
  }
  .card-front { background: var(--teal); }
  .texture { position: absolute; inset: 0; background: var(--teal); }
  .front-mark {
    position: absolute; inset: 0;
    display: flex; align-items: center; justify-content: center; gap: 14px;
  }
  .mark-dot {
    width: 22px; height: 22px; border-radius: 50%;
    background: var(--slate);
  }
  .mark-name {
    font-weight: 700; font-size: 30px; color: var(--slate);
    text-align: center; line-height: 1.15;
  }
  .card-back { background: var(--paper); }
  .back-mark {
    position: absolute; left: 36px; top: 0; bottom: 0; width: 200px;
    display: flex; align-items: center; justify-content: center; gap: 10px;
  }
  .back-mark .mark-name { font-size: 22px; }
  .back-mark .mark-dot { width: 16px; height: 16px; }
  .details {
    position: absolute; left: 262px; top: 48px; right: 20px;
    color: var(--ink); font-size: 13px; line-height: 1.45;
  }
  .person-name { color: var(--teal-dark); font-size: 27px; font-weight: 700; line-height: 1.05; }
  .person-title { font-size: 13px; margin-bottom: 14px; }
  .licenses { margin-bottom: 14px; }
  .contact-list { list-style: none; }
  .contact-list li { display: flex; align-items: center; gap: 8px; }
  .contact-list svg { width: 12px; height: 12px; flex: none; fill: var(--slate); }
</style>
</head>
<body>
<main class="stage">
  <section class="card card-front">
    <div class="texture" role="img" aria-label="Distressed white crackle texture over teal"></div>
    <div class="front-mark">
      <span class="mark-dot"></span>
      <span class="mark-name">Copperline<br>Pipeworks, Inc.</span>
    </div>
  </section>

  <section class="card card-back">
    <div class="back-mark">
      <span class="mark-dot"></span>
      <span class="mark-name">Copperline<br>Pipeworks, Inc.</span>
    </div>
    <div class="details">
      <h1 class="person-name">Glen Harwick</h1>
      <p class="person-title">President</p>
      <p class="licenses">Nevada License #64205<br>California License #5870413</p>
      <ul class="contact-list">
        <li><svg viewBox="0 0 24 24"><path d="M6.6 10.8a15 15 0 0 0 6.6 6.6l2.2-2.2c.3-.3.7-.4 1-.2 1.1.4 2.3.6 3.6.6.6 0 1 .4 1 1V20c0 .6-.4 1-1 1A17 17 0 0 1 3 4c0-.6.4-1 1-1h3.5c.6 0 1 .4 1 1 0 1.3.2 2.5.6 3.6.1.3 0 .7-.2 1z"/></svg>(555) 630-2918</li>
        <li><svg viewBox="0 0 24 24"><path d="M7 1h10a2 2 0 0 1 2 2v18a2 2 0 0 1-2 2H7a2 2 0 0 1-2-2V3a2 2 0 0 1 2-2zm0 3v14h10V4zm5 15.5a1 1 0 1 0 0 2 1 1 0 0 0 0-2z"/></svg>(555) 418-9063</li>
        <li><svg viewBox="0 0 24 24"><path d="M2 5h20v14H2zm2 2v.5l8 5 8-5V7l-8 5z"/></svg>glen@copperlinepipeworks.example</li>
        <li><svg viewBox="0 0 24 24"><path d="M12 2a10 10 0 1 0 0 20 10 10 0 0 0 0-20zm6.9 9h-3a15 15 0 0 0-1.3-5.6A8 8 0 0 1 18.9 11zM12 4c.9 1.3 1.8 3.8 1.9 7h-3.8c.1-3.2 1-5.7 1.9-7zM9.4 5.4A15 15 0 0 0 8.1 11h-3a8 8 0 0 1 4.3-5.6zM5.1 13h3a15 15 0 0 0 1.3 5.6A8 8 0 0 1 5.1 13zm6.9 7c-.9-1.3-1.8-3.8-1.9-7h3.8c-.1 3.2-1 5.7-1.9 7zm2.6-1.4a15 15 0 0 0 1.3-5.6h3a8 8 0 0 1-4.3 5.6z"/></svg>www.copperlinepipeworks.example</li>
      </ul>
    </div>
  </section>
</main>
</body>
</html>
```